Exciting New Reseller Brand requires Website to WOW New clients to register.

We are a NEW online business called Trade Your Goods.

The Website is a simple concept, it looks to put Merchants (businesses that want their products resold) in touch with Resellers (people or businesses that want to resell that product).

The website acts as an online market place which looks to get Merchants to sign-up and pay to list their company and product as well as getting Resellers to sign-up to view potential Merchants they can get in touch with in the right industry or area to resell their products for (see attached slide-pack to explain packages)

Any type of Industry or Business can register themselves to get listed on Trade Your Goods to see either get their product/service resold or to look for products / services to reseller.

Trade Your Goods does not take any other monetary part in the business relationships other than to obtain money for the monthly website subscription.

We want a very simple website, so this project is for several pages:

Page 1) A really vibrant, exciting, image based homepage to get people to sign-up / register (see sites that we like in the project brief). Needs to be very clear that there are 2 customers and to sign up to join, build and earn!

Page 2) A page that describes the benefits and packages for Resellers.

Page 3) A page that describes the benefits and packages for Merchants.

Page 4) The Payment process pages, taking the customer through sign-up

Page 5) The Business Listings page, so when people search for a Merchant how this will be displayed.

We would really like an image based site and preferably parallax. We want it bright vibrant and to look like a social media site.

All necessary files / logos enclosed.

We would love to continue to work with the winning designer moving forward.

Many thanks and Good Luck.

Regards

Martin & Owen

Target Market(s)

Merchants, Suppliers, Vendors, Manufacturers, Distributors, Wholesalers, Affiliate programs, Franchisees, Reselers

Industry/Entity Type

Business

Number of Pages Required

5+ page

Requirements
Must have
• We love the following websites:
• 1) Like the top section, i.e. parallax image based: www.brightfoxstudio.co.uk
• 2) Like the way the screen is split in 2, could be used to describe the 2 different customers we are after Merchants / Resellers: www.cloudtrunk.example/guide
• 3) Like the bright colours / full screen video split into 2 below top banner and the generally how simple the site is: www.harbourlinden.com.au
• 4) Love all of this site, simple, bold, Love the colours, the clear message and the infographics: http://www.velomiro.example/swiftride/quicker

```html
<!DOCTYPE html>
<html lang="en">
<head>
<meta charset="utf-8">
<title>Trade Your Goods – Join · Build · Earn</title>
<link href="https://fonts.googleapis.com/css2?family=Open+Sans:wght@400;600;700;800&family=Oswald:wght@400;500&display=swap" rel="stylesheet">
<style>
  :root{
    --blue:#2a9fd8;
    --blue-deep:#1f8fca;
    --green:#8cc63f;
    --ink:#3b2c2c;
    --text:#555;
    --muted:#999;
    --light:#ececec;
    --card:#ffffff;
    --footer:#3b3e43;
    --footer-deep:#2d2f33;
    --white:#ffffff;
  }
  *{box-sizing:border-box;margin:0;padding:0}
  html,body{width:1200px;height:3297px;overflow:hidden}
  body{font-family:"Open Sans",Arial,sans-serif;color:var(--text);background:var(--white);position:relative}

  /* Hero */
  .hero{position:relative;height:587px;overflow:hidden}
  .hero-photo{position:absolute;inset:0;background:linear-gradient(120deg,#2b2a2c 0%,#4b4746 35%,#6b655f 60%,#3a3837 100%)}
  .hero-shade{position:absolute;inset:0;background:linear-gradient(180deg,rgba(0,0,0,.35),rgba(0,0,0,.15) 50%,rgba(0,0,0,.35))}
  .utility{position:absolute;top:8px;right:70px;display:flex;align-items:center;gap:8px;font-size:11px;color:var(--white)}
  .utility .sq{width:16px;height:16px;background:rgba(255,255,255,.75);border-radius:2px}
  .utility .links{margin-right:10px}
  .masthead{position:absolute;top:52px;left:110px;right:40px;display:flex;justify-content:space-between;align-items:center}
  .brand{display:flex;align-items:center;gap:12px;color:var(--white);font-weight:700;font-size:30px;letter-spacing:-.5px}
  .brand .mark{width:44px;height:44px;border-radius:50%;background:var(--white)}
  .nav{display:flex;gap:34px;list-style:none;font-size:13px;color:var(--white);font-weight:600}
  .hero-copy{position:absolute;top:268px;left:0;right:0;text-align:center;color:var(--white)}
  .hero-copy .kicker{font-size:34px;font-weight:400;letter-spacing:1px}
  .hero-copy .slogan{font-size:58px;font-weight:800;letter-spacing:2px;margin-top:4px}
  .hero-arrow{position:absolute;top:280px}
  .hero-arrow.left{left:8px}.hero-arrow.right{right:8px}
  .scroll-cue{position:absolute;left:50%;top:478px;transform:translateX(-50%)}

  /* Split */
  .split{display:flex;height:303px}
  .split-panel{flex:1;text-align:center;color:var(--white);padding-top:40px}
  .split-panel.merchants{background:var(--blue)}
  .split-panel.resellers{background:var(--green)}
  .split-panel h2{font-size:52px;font-weight:700;line-height:1}
  .split-panel h3{font-size:22px;font-weight:700;margin-top:6px}
  .split-panel p{font-size:13px;line-height:1.5;width:460px;margin:18px auto 0}
  .split-panel .btn{display:inline-block;margin-top:16px;border:1px solid var(--white);background:var(--white);color:var(--ink);font-size:12px;padding:5px 34px;font-weight:600}

  /* Intro */
  .intro{height:380px;background:var(--light);text-align:center;padding-top:92px}
  .intro h2{font-size:44px;font-weight:600;color:var(--ink);line-height:1.2}
  .intro h2 em{font-style:normal;color:var(--green)}
  .intro p{width:900px;margin:34px auto 0;font-size:15px;line-height:1.65;color:#444}

  /* Benefits */
  .benefits{position:relative;height:418px;overflow:hidden;text-align:center}
  .benefits-photo{position:absolute;inset:0;background:linear-gradient(100deg,#2a2625 0%,#5c534c 40%,#3a3431 70%,#1f1d1c 100%)}
  .benefits-inner{position:relative;padding-top:100px}
  .benefits h2{font-family:"Oswald","Open Sans",sans-serif;font-weight:500;font-size:66px;color:var(--white);letter-spacing:1px}
  .benefit-links{display:flex;justify-content:center;gap:28px;margin-top:34px}
  .benefit-links span{width:285px;height:90px;border:3px solid var(--white);display:flex;align-items:center;justify-content:center;color:var(--white);font-size:28px;background:rgba(0,0,0,.35)}

  /* Posts */
  .posts{height:1142px;background:#f4f4f4;position:relative}
  .posts h2{text-align:center;font-size:40px;font-weight:600;color:var(--ink);padding-top:32px}
  .post-grid{position:absolute;top:124px;left:16px;right:40px;display:flex;gap:20px;align-items:flex-start}
  .post-col{flex:1;display:flex;flex-direction:column;gap:22px}
  .post{background:var(--card);box-shadow:0 1px 2px rgba(0,0,0,.08)}
  .post-media{position:relative}
  .post-media .photo{display:block}
  .date-tag{position:absolute;top:0;left:0;width:36px;background:var(--blue);color:var(--white);text-align:center;font-size:10px;padding:4px 0}
  .date-tag b{display:block;font-size:19px;line-height:1.1}
  .post-body{padding:14px 16px 16px}
  .post-body h4{font-size:17px;font-weight:600;color:#333;line-height:1.3}
  .post-body p{font-size:12px;line-height:1.55;color:#777;margin-top:8px}
  .post-body .more{font-size:12px;color:#444;margin-top:10px;font-weight:600}
  .post-body .meta{font-size:11px;color:var(--muted);margin-top:8px}
  .load-more{position:absolute;bottom:0;left:0;right:0;height:60px;text-align:center}
  .load-more span{display:inline-block;margin-top:18px;font-size:14px;color:#666}

  /* CTA */
  .cta{position:relative;height:170px;overflow:hidden}
  .cta-photo{position:absolute;inset:0;background:linear-gradient(90deg,#9a9c9e,#c7c8c9 50%,#9fa1a3)}
  .cta-bar{position:absolute;left:92px;right:106px;top:38px;height:92px;background:var(--blue-deep);border:4px solid var(--white);display:flex;align-items:center;justify-content:center;color:var(--white);font-size:36px;font-weight:700}

  /* Footer */
  .site-footer{height:265px;background:var(--footer);display:flex;padding:48px 100px 0 110px;gap:50px;color:#bbb;font-size:12px;line-height:1.7}
  .site-footer .brand{font-size:30px;margin-top:24px}
  .site-footer .brand .mark{background:var(--blue)}
  .footer-col{width:210px}
  .footer-col.wide{width:330px}
  .footer-col h5{color:var(--white);font-size:13px;font-weight:700;margin-bottom:8px;letter-spacing:.5px}
  .footer-icons{display:flex;gap:10px;margin-top:14px}
  .footer-icons i{width:16px;height:16px;border-radius:50%;background:#8a8d92;display:block}
  .legal{height:32px;background:var(--footer-deep);font-size:11px;color:#888;padding:8px 110px}
</style>
</head>
<body>

<header class="hero">
  <div class="hero-photo" role="img" aria-label="Photo of a person working on a laptop at a desk"></div>
  <div class="hero-shade"></div>
  <div class="utility"><span class="links">Sign in | Register</span><span class="sq"></span><span class="sq"></span><span class="sq"></span></div>
  <div class="masthead">
    <div class="brand"><span class="mark"></span>Trade Your Goods</div>
    <ul class="nav"><li>HOME</li><li>MERCHANTS</li><li>RESELLER</li><li>PRICING</li><li>FAQ'S</li><li>CONTACT US</li></ul>
  </div>
  <svg class="hero-arrow left" width="20" height="24" viewBox="0 0 20 24"><path d="M14 3 L5 12 L14 21" fill="none" stroke="#fff" stroke-width="2.5"/></svg>
  <svg class="hero-arrow right" width="20" height="24" viewBox="0 0 20 24"><path d="M6 3 L15 12 L6 21" fill="none" stroke="#fff" stroke-width="2.5"/></svg>
  <div class="hero-copy">
    <div class="kicker">BUILDING YOU OWN VIRTUAL SALES TEAM</div>
    <div class="slogan">JOIN · BUILD · EARN</div>
  </div>
  <svg class="scroll-cue" width="48" height="48" viewBox="0 0 48 48"><circle cx="24" cy="24" r="22" fill="rgba(255,255,255,.25)" stroke="#fff" stroke-width="2"/><path d="M15 19 L24 28 L33 19" fill="none" stroke="#fff" stroke-width="3"/></svg>
</header>

<section class="split">
  <div class="split-panel merchants">
    <h2>MERCHANTS</h2>
    <h3>Register To Build Your Virtual Sales Team</h3>
    <p>List your products once and let motivated resellers across every region carry them to new buyers. Your team grows while you focus on making great goods.</p>
    <span class="btn">BUILD</span>
  </div>
  <div class="split-panel resellers">
    <h2>RESELLERS</h2>
    <h3>Register To Start Earning Money</h3>
    <p>Browse trusted merchants in your industry or area, pick the products you believe in and start earning from every sale you make to your own network.</p>
    <span class="btn">EARN</span>
  </div>
</section>

<section class="intro">
  <h2>Bringing Reseller Opportunities<br>to the <em>masses..</em></h2>
  <p>Praesent eget lorem vitae mauris interdum luctus convallis a nunc. Phasellus dictum placerat volutpat. Cras facilisis quam lacus, molestie bibendum nisi egestas nec. Quisque vitae velit posuere, faucibus libero a, posuere felis. Nullam sit amet ornare lectus. Etiam adipiscing elit viverra.</p>
</section>

<section class="benefits">
  <div class="benefits-photo" role="img" aria-label="Photo of a business team giving thumbs up"></div>
  <div class="benefits-inner">
    <h2>BENEFITS FOR EVERYONE</h2>
    <div class="benefit-links"><span>MERCHANTS</span><span>RESELLERS</span></div>
  </div>
</section>

<section class="posts">
  <h2>Helping Businesses &amp; Resellers</h2>
  <div class="post-grid">
    <div class="post-col">
      <article class="post">
        <div class="post-media"><svg class="photo" width="100%" height="205" role="img" aria-label="Photo of printed business cards on a table"><rect width="100%" height="100%" fill="#c9c2b6"/></svg><div class="date-tag">Sep<b>25</b>2014</div></div>
        <div class="post-body"><h4>Modern business cards</h4><p>Duis aenean, est eu tempus sed lectus at diam nec, sit augue felis lorem odio vel tempus ultrices.</p><div class="more">Read details »</div><div class="meta">0 Comments | Design</div></div>
      </article>
      <article class="post">
        <div class="post-media"><svg class="photo" width="100%" height="190" role="img" aria-label="Photo of a weather app on a phone screen"><rect width="100%" height="100%" fill="#4b4660"/></svg><div class="date-tag">Aug<b>6</b>2014</div></div>
        <div class="post-body"><h4>Weather mobile app</h4><p>Etiam ultrices orci leo, in feugiat enim tristique et. Proin lorem fusce dolor gravida ligula justo, iaculis quis.</p><div class="more">Read details »</div><div class="meta">0 Comments | Web</div></div>
      </article>
    </div>
    <div class="post-col">
      <article class="post">
        <div class="post-media"><svg class="photo" width="100%" height="265" role="img" aria-label="Photo of a hand holding a phone with a music app"><rect width="100%" height="100%" fill="#cfd6dc"/></svg><div class="date-tag">Sep<b>26</b>2014</div></div>
        <div class="post-body"><h4>Mobile music app</h4><p>Proin eget magna in sagittis erat. Etiam ultrices sem felis. Proin ligula quam, porta in vulputate non, sed amet volutpat risus.</p><div class="more">Read details »</div><div class="meta">0 Comments | Video &amp; Music</div></div>
      </article>
      <article class="post">
        <div class="post-media"><svg class="photo" width="100%" height="195" role="img" aria-label="Photo of dark business cards stacked"><rect width="100%" height="100%" fill="#3a3b3e"/></svg></div>
        <div class="post-body"><h4>Business cards design trends</h4><p>Vehicula orci leo, in feugiat enim tristique et. Proin lorem fusce dolor gravida ligula justo, iaculis quis semper et purus. Nam sed ultrices augue lorem sed.</p><div class="more">Read details »</div><div class="meta">0 Comments | Photography</div></div>
      </article>
    </div>
    <div class="post-col">
      <article class="post">
        <div class="post-media"><svg class="photo" width="100%" height="180" role="img" aria-label="Photo of a dark business card on a black surface"><rect width="100%" height="100%" fill="#2c2d30"/></svg><div class="date-tag">Sep<b>5</b>2014</div></div>
        <div class="post-body"><h4>Frozen emotions</h4><p>Vivamus aliquam blandit sapien, a suscipit nisi convallis vellam gravida felis nec. Fusce molestie sed interdum.</p><div class="more">Read details »</div><div class="meta">0 Comments | Video &amp; Music</div></div>
      </article>
      <article class="post">
        <div class="post-media"><svg class="photo" width="100%" height="265" role="img" aria-label="Photo of a hand holding a phone with a music app"><rect width="100%" height="100%" fill="#d8dde1"/></svg><div class="date-tag">Nov<b>28</b>2014</div></div>
        <div class="post-body"><h4>Mobile music app</h4><p>Proin eget magna in sagittis erat. Etiam ultrices sem felis. Proin ligula quam, porta in vulputate non, sit amet volutpat.</p><div class="more">Read details »</div><div class="meta">0 Comments | Video &amp; Music</div></div>
      </article>
    </div>
    <div class="post-col">
      <article class="post">
        <div class="post-media"><svg class="photo" width="100%" height="205" role="img" aria-label="Photo of a creative team around a meeting table"><rect width="100%" height="100%" fill="#cdd3d8"/></svg><div class="date-tag">Mar<b>4</b>2014</div></div>
        <div class="post-body"><h4>How to choose a perfect creative agency</h4><p>Vestibulum feugiat dolor molestie feugiat volutpat. Donec sed vulputate enim, non varius justo. Aenean a orci egestas, blandit nisi quis congue justo.</p><div class="more">Read details »</div><div class="meta">0 Comments | Design</div></div>
      </article>
      <article class="post">
        <div class="post-media"><svg class="photo" width="100%" height="225" role="img" aria-label="Photo of a lit bridge over water at dusk"><rect width="100%" height="100%" fill="#4a5e86"/></svg></div>
        <div class="post-body"><h4>Most beautiful world bridges</h4><p>Vivamus aliquam blandit sapien, a suscipit nisi gravida sollicitudin felis nec ullamcorper risus molestie scelerisque.</p><div class="more">Read details »</div><div class="meta">0 Comments | Photography</div></div>
      </article>
    </div>
  </div>
  <div class="load-more">
    <svg width="60" height="10" viewBox="0 0 60 10" style="display:block;margin:0 auto"><path d="M0 10 L30 0 L60 10" fill="none" stroke="#ccc"/></svg>
    <span>Load more</span>
  </div>
</section>

<section class="cta">
  <div class="cta-photo" role="img" aria-label="Faded photo of a group of business people"></div>
  <div class="cta-bar">FIND YOUR IDEAL BUSINESS PARTNER MATCH NOW</div>
</section>

<footer class="site-footer">
  <div class="footer-col">
    <div class="brand"><span class="mark"></span>Trade Your Goods</div>
  </div>
  <div class="footer-col">
    <div>Suite 4, Harbour Row</div>
    <div>12 Market Street</div>
    <div>Nashville, TN 37201</div>
    <div>Email: hello@tradeyourgoods.example</div>
    <div>Phone: +00 (0) 123 456 789</div>
    <div>Fax: +00 (0) 123 456 780</div>
    <div class="footer-icons"><i></i><i></i><i></i><i></i><i></i><i></i></div>
  </div>
  <div class="footer-col">
    <h5>RECENT POSTS</h5>
    <div>Donec Pellentesque Tempus</div>
    <div>Adipiscing semper nisi</div>
    <div>Vel eleifend ullamcorper velit</div>
    <div>Quisque gravida luctus</div>
    <div>Curabitur ac neque at eros</div>
  </div>
  <div class="footer-col">
    <h5>POPULAR POSTS</h5>
    <div>Donec Pellentesque Tempus</div>
    <div>Adipiscing semper nisi</div>
    <div>Vel eleifend ullamcorper velit</div>
    <div>Quisque gravida luctus</div>
    <div>Curabitur ac neque at eros</div>
  </div>
</footer>
<div class="legal">© 2014 Trade Your Goods. All rights reserved.</div>

</body>
</html>
```